Brave Roads Ahead: Holding Hope, Meeting Storms, Voicing Triumph

I want a modern and clean looking book cover. 5.25x8

Title
Brave Roads Ahead

Subtitle
Holding Hope, Meeting Storms, Voicing Triumph

I don’t just want a graphic, I want it to make sense. If it can just be the words and a textured looking background, I’ll be ok with that too. I just want it to look crisp, clean, modern.

I want the back to have my book blurb and bio attached with the pic that’s attached.

Target Market(s)

Self help

Requirements
Must have
• Modern, clean look, look professional, attract customers.

```html
<!DOCTYPE html>
<html lang="en">
<head>
<meta charset="utf-8">
<title>Brave Roads Ahead — Book Cover</title>
<link rel="stylesheet" href="https://fonts.googleapis.com/css2?family=Bodoni+Moda:opsz,wght@6..96,400;6..96,500;6..96,600&display=swap">
<style>
  :root {
    --paper-light: #fbfbfc;
    --paper-mid: #eceef0;
    --paper-shade: #d9dcdf;
    --ink: #111111;
    --plum: #8e1f5a;
    --berry: #c01a52;
    --crimson: #ff0a3c;
    --coral: #f04a4a;
    --tangerine: #f7942a;
    --flame: #ff5a2a;
  }
  * { margin: 0; padding: 0; box-sizing: border-box; }
  html, body {
    width: 788px;
    height: 1200px;
    overflow: hidden;
    background: var(--paper-light);
  }
  .cover {
    position: relative;
    width: 788px;
    height: 1200px;
    overflow: hidden;
    font-family: "Bodoni Moda", "Didot", serif;
  }
  .cover__texture {
    position: absolute;
    inset: 0;
    background:
      radial-gradient(ellipse 60% 40% at 75% 55%, rgba(190,194,198,0.45), transparent 70%),
      radial-gradient(ellipse 50% 35% at 20% 80%, rgba(205,208,212,0.4), transparent 70%),
      radial-gradient(ellipse 45% 30% at 60% 15%, rgba(215,218,222,0.35), transparent 70%),
      linear-gradient(160deg, var(--paper-light) 0%, var(--paper-mid) 55%, var(--paper-shade) 100%);
  }
  .title {
    position: absolute;
    left: 74px;
    top: 60px;
    font-weight: 500;
    font-size: 214px;
    line-height: 235px;
    letter-spacing: -2px;
  }
  .title__line {
    display: block;
    width: max-content;
    -webkit-background-clip: text;
    background-clip: text;
    color: transparent;
  }
  .title__line--first  { background-image: linear-gradient(90deg, var(--plum) 0%, var(--coral) 50%, var(--tangerine) 90%); }
  .title__line--second { background-image: linear-gradient(90deg, var(--berry) 0%, var(--coral) 45%, var(--tangerine) 85%); }
  .title__line--third  { background-image: linear-gradient(90deg, var(--crimson) 0%, var(--coral) 55%, var(--flame) 95%); }
  .subtitle {
    position: absolute;
    left: 76px;
    top: 790px;
    width: 560px;
    font-size: 31px;
    line-height: 36px;
    font-weight: 400;
    color: var(--ink);
  }
  .author {
    position: absolute;
    left: 74px;
    top: 1068px;
    font-size: 44px;
    font-weight: 500;
    color: var(--ink);
  }
</style>
</head>
<body>
  <main class="cover">
    <div class="cover__texture" role="img" aria-label="Crumpled white paper texture background"></div>
    <h1 class="title">
      <span class="title__line title__line--first">Brave</span>
      <span class="title__line title__line--second">Roads</span>
      <span class="title__line title__line--third">Ahead</span>
    </h1>
    <p class="subtitle">Holding Hope, Meeting Storms, Voicing Triumph</p>
    <p class="author">Marisa Holden</p>
  </main>
</body>
</html>
```